I am looking for a flyer design for my upcoming symposium. Here are the details for the flyer and pictures of speakers are attached.

Name of Symposium: Lattice and Pathway Biosciences Symposium, Sponsored by the Corvale Chromatin Institute and the Department of Bioengineering
Date: January 8, 2018
Location: Havergill Auditorium, Tarnby Center for Applied Discovery, 2175 Orchard Terrace Ave, Philadelphia, PA 19127

Reception to follow after the symposium.

Also, please add - Register and upload abstracts for the symposium at www.qzvmrk.com. Registration and abstract submission closes on January 4, 2018.

Keynote Speaker:
Marthe Quillon, Ph.D.
NTVO Director General; Professor, Lyceum of Norvane; Director, Genetics and Developmental Biology at Institut Bramoux
Lyceum of Norvane, NTVO, Institut Bramoux
"Title of talk TBA."

Speakers:
Lena Drewcott, Ph.D.
Assistant Professor of Cell and Developmental Biology
Halvering State University, HMCS
"Title of talk TBA."

Paul Marden, Ph.D.
Assistant Professor of Genetics
"Title of talk TBA."

Ilse Varga, Ph.D.
Professor, Ostrander University
Otto Wenzlau Center for Molecular Medicine
"Title of talk TBA."

Jun Hao, Ph.D.
Professor of Cellular and Molecular Medicine
Coastal Meridian University
"Title of talk TBA."

Wei Lun, Ph.D.
Associate Professor of Pediatrics
The Youth Medical Pavilion of Philadelphia
"Spatial genome re-organization between fetal and adult hematopoietic stem cells."

Mei Zhou, Ph.D.
Professor, Department of Genetics
Ellsworth Medical School
"Title of talk TBA."

```html
<!DOCTYPE html>
<html lang="en">
<head>
<meta charset="utf-8">
<title>Lattice and Pathway Biosciences Symposium</title>
<link href="https://fonts.googleapis.com/css2?family=Anton&family=Lato:wght@400;700;900&family=Montserrat:wght@700;800&family=Oswald:wght@500&display=swap" rel="stylesheet">
<style>
  :root {
    --red: #d9151f;
    --red-deep: #a80d16;
    --blue: #1a63ad;
    --blue-deep: #0b3f86;
    --footer-blue: #2f72b5;
    --gray-band: #ececec;
    --ink: #1d1d1d;
    --white: #ffffff;
  }
  * { box-sizing: border-box; margin: 0; padding: 0; }
  html, body { width: 846px; height: 1200px; overflow: hidden; background: #ffffff; }
  body { font-family: "Lato", sans-serif; color: var(--ink); }
  .flyer { position: relative; width: 846px; height: 1200px; overflow: hidden; background: var(--white); }

  .hero { position: absolute; left: 0; top: 0; width: 846px; height: 390px; overflow: hidden; }
  .hero-art { position: absolute; inset: 0;
    background:
      radial-gradient(ellipse at 78% 70%, rgba(120,190,255,.55), transparent 45%),
      radial-gradient(ellipse at 18% 20%, rgba(255,90,90,.45), transparent 50%),
      linear-gradient(100deg, #c8121c 0%, #b4141f 30%, #8a2d55 50%, #2a5aa6 66%, #0f4a96 100%); }
  .title-frame { position: absolute; left: 0; top: 0; }
  .title-top, .title-main, .title-bottom { position: absolute; left: 0; width: 846px; text-align: center; color: var(--white); }
  .title-top { top: 56px; font-family: "Montserrat", sans-serif; font-weight: 800; font-size: 34px; letter-spacing: -.5px; }
  .title-main { top: 92px; font-family: "Anton", sans-serif; font-size: 92px; line-height: 1.1; letter-spacing: 1px; }
  .title-bottom { top: 192px; font-family: "Montserrat", sans-serif; font-weight: 800; font-size: 48px; letter-spacing: .5px; }

  .sponsor { position: absolute; top: 305px; height: 57px; background: var(--white); display: flex; align-items: center; gap: 8px; padding: 0 10px; }
  .sponsor--institute { left: 252px; width: 165px; }
  .sponsor--engineering { left: 457px; width: 142px; }
  .sponsor-mark { width: 18px; height: 18px; flex: none; }
  .sponsor-name { font-family: "Lato", sans-serif; font-weight: 700; font-size: 14px; line-height: 1.1; color: var(--blue-deep); }

  .event-band { position: absolute; left: 0; top: 390px; width: 846px; height: 127px; background: var(--red); color: var(--white); }
  .event-date { position: absolute; left: 52px; top: 32px; font-family: "Oswald", sans-serif; font-weight: 500; font-size: 46px; line-height: 1; letter-spacing: -.5px; }
  .event-venue { position: absolute; left: 369px; top: 26px; font-size: 17.5px; line-height: 1.3; }
  .event-venue strong { font-weight: 900; }

  .keynote { position: absolute; left: 0; top: 517px; width: 846px; height: 191px; background: var(--gray-band); }
  .keynote-photo { position: absolute; left: 157px; top: 19px; width: 134px; height: 136px; }
  .keynote-info { position: absolute; left: 309px; top: 20px; }
  .keynote-label { font-weight: 700; font-size: 23px; color: var(--blue); }
  .keynote-name { margin-top: 6px; border-left: 2px solid var(--red); padding-left: 8px; font-size: 15px; line-height: 1.25; }
  .keynote-name b { font-weight: 700; font-size: 22px; color: var(--red); }
  .talk { color: var(--blue); }

  .speakers { position: absolute; left: 0; top: 708px; width: 846px; height: 409px; }
  .speaker { position: absolute; width: 360px; }
  .speaker-photo { position: absolute; left: 0; top: 0; width: 104px; height: 104px; }
  .speaker-info { position: absolute; left: 126px; top: 20px; width: 240px; border-left: 2px solid var(--red); padding-left: 6px; font-size: 11.5px; line-height: 1.25; }
  .speaker-name { font-weight: 700; font-size: 13px; color: var(--red); }
  .speaker-name span, .keynote-name span { font-weight: 400; color: var(--ink); font-size: .85em; }

  .registration { position: absolute; left: 0; top: 1117px; width: 846px; height: 83px; background: var(--footer-blue); color: var(--white); text-align: center; }
  .registration-main { margin-top: 16px; font-weight: 700; font-size: 21px; }
  .registration-note { font-size: 15.5px; margin-top: 3px; }
</style>
</head>
<body>
<main class="flyer">
  <header class="hero">
    <div class="hero-art" role="img" aria-label="Red-to-blue background with a glowing DNA double helix"></div>
    <svg class="title-frame" width="846" height="390" viewBox="0 0 846 390">
      <path d="M160 70 H125 V248 H170 M686 70 H719 V248 H678" fill="none" stroke="#ffffff" stroke-width="3"/>
    </svg>
    <div class="title-top">LATTICE &amp; PATHWAY</div>
    <div class="title-main">BIOSCIENCES</div>
    <div class="title-bottom">SYMPOSIUM</div>
    <div class="sponsor sponsor--institute">
      <svg class="sponsor-mark" viewBox="0 0 18 18"><rect width="18" height="18" fill="#0b3f86"/></svg>
      <span class="sponsor-name">Corvale Chromatin Institute</span>
    </div>
    <div class="sponsor sponsor--engineering">
      <svg class="sponsor-mark" viewBox="0 0 18 18"><rect width="18" height="18" fill="#0b3f86"/></svg>
      <span class="sponsor-name">Marlow Engineering</span>
    </div>
  </header>

  <section class="event-band">
    <div class="event-date">JANUARY 8, 2018</div>
    <div class="event-venue">
      <strong>Havergill Auditorium, Tarnby Center</strong><br>
      <strong>for Applied Discovery,</strong><br>
      2175 Orchard Terrace Ave, Philadelphia, PA 19127
    </div>
  </section>

  <section class="keynote">
    <div class="keynote-photo" role="img" aria-label="Portrait of keynote speaker Marthe Quillon" style="background:linear-gradient(160deg,#c9b7a6,#7a5a48)"></div>
    <div class="keynote-info">
      <div class="keynote-label">Keynote Speaker:</div>
      <div class="keynote-name">
        <b>Marthe Quillon,</b> <span>Ph.D.</span><br>
        NTVO Director General; Professor, Lyceum of Norvane;<br>
        Director, Genetics and Developmental Biology at Institut Bramoux<br>
        Lyceum of Norvane, NTVO, Institut Bramoux<br>
        <span class="talk">"Title of talk TBA."</span>
      </div>
    </div>
  </section>

  <section class="speakers">
    <article class="speaker" style="left:63px;top:25px">
      <div class="speaker-photo" role="img" aria-label="Portrait of Lena Drewcott" style="background:linear-gradient(160deg,#8c6f5a,#3e2c24)"></div>
      <div class="speaker-info">
        <div class="speaker-name">Lena Drewcott, <span>Ph.D.</span></div>
        Assistant Professor of Cell and<br>Developmental Biology<br>Halvering State University, HMCS<br>
        <span class="talk">"Title of talk TBA."</span>
      </div>
    </article>
    <article class="speaker" style="left:475px;top:25px">
      <div class="speaker-photo" role="img" aria-label="Portrait of Paul Marden" style="background:linear-gradient(160deg,#a0453a,#5a2a22)"></div>
      <div class="speaker-info">
        <div class="speaker-name">Paul Marden, <span>Ph.D.</span></div>
        Assistant Professor of Genetics<br>Halvering State University, HMCS<br>
        <span class="talk">"Title of talk TBA."</span>
      </div>
    </article>
    <article class="speaker" style="left:63px;top:144px">
      <div class="speaker-photo" role="img" aria-label="Portrait of Ilse Varga" style="background:linear-gradient(160deg,#6e665c,#2f2a26)"></div>
      <div class="speaker-info">
        <div class="speaker-name">Ilse Varga, <span>Ph.D.</span></div>
        Professor, Ostrander University<br>Otto Wenzlau Center for Molecular<br>Medicine<br>
        <span class="talk">"Title of talk TBA."</span>
      </div>
    </article>
    <article class="speaker" style="left:475px;top:144px">
      <div class="speaker-photo" role="img" aria-label="Portrait of Jun Hao" style="background:linear-gradient(160deg,#7f8a5a,#3b3a2c)"></div>
      <div class="speaker-info">
        <div class="speaker-name">Jun Hao, <span>Ph.D.</span></div>
        Professor of Cellular and Molecular<br>Medicine<br>Coastal Meridian University<br>
        <span class="talk">"Title of talk TBA."</span>
      </div>
    </article>
    <article class="speaker" style="left:63px;top:262px">
      <div class="speaker-photo" role="img" aria-label="Portrait of Wei Lun" style="background:linear-gradient(160deg,#4d7fb8,#27425e)"></div>
      <div class="speaker-info">
        <div class="speaker-name">Wei Lun, <span>Ph.D.</span></div>
        Associate Professor of Pediatrics<br>The Youth Medical Pavilion of Philadelphia<br>
        <span class="talk">"Spatial genome re-organization between<br>fetal and adult hematopoietic stem cells."</span>
      </div>
    </article>
    <article class="speaker" style="left:475px;top:262px">
      <div class="speaker-photo" role="img" aria-label="Portrait of Mei Zhou" style="background:linear-gradient(160deg,#5f7a4a,#2d3a24)"></div>
      <div class="speaker-info">
        <div class="speaker-name">Mei Zhou, <span>Ph.D.</span></div>
        Professor, Department of Genetics<br>Ellsworth Medical School<br>
        <span class="talk">"Title of talk TBA."</span>
      </div>
    </article>
  </section>

  <footer class="registration">
    <div class="registration-main">Register and upload abstracts for the symposium at www.qzvmrk.com.</div>
    <div class="registration-note">Registration and abstract submission closes on January 4, 2018.</div>
  </footer>
</main>
</body>
</html>
```